Maple Syrup Bottle (front) Label design

I need label design for a 16fl OZ rectangular bottle of maple syrup with the usable dimensions of: Front: 4" x 2" and the back area for "ingredient specifications" of: 6" x 2". The maple syrup product comes from our own farm and is a quality product. The technical name/class of the syrup is: Grade A / AMBER
Updates

I can’t seem to find a way to upload a photo of the maple syrup bottle, but the front dimensions are clearly written on bottle description. Again: 4.5” by 2.25”

I have tried to upload the photo of the maple syrup bottle several times, and it seems (from my side) that it is successful. But I can never find it and the artists cannot find it either. Not sure what to do.

I have tried several times to add a photo of maple bottle, but it never shows up

This seems to be a futile exercise

I would like to post some images of the actual quill Hollow (not the one on Fendix, though!
But I can’t get back to the page that allows that to happen. Please advise!

Somebody PLEASE ask PW management to make it possible for me to upload more images! The "add photos" etc. just disappears from anywhere.

Target Market(s)

High-end food stores

Industry/Entity Type

Maple syrup retail industry

Other font styles liked:
• I don't know, and welcome suggestions

Colors

Designer to choose colors to be used in the design.

Requirements
Must have
• Name of Farm: Quill Hollow Maple
Nice to have
• The label can be "minimalist" and elegant. There is already a Maple leaf glass relief on the top of front of the bottle.
Should not have
• and NOT include farm buildings with steam coming out the chimney, etc.

```html
<!DOCTYPE html>
<html lang="en">
<head>
<meta charset="utf-8">
<title>Quill Hollow Maple – Maple Syrup Front Label</title>
<link rel="stylesheet" href="https://fonts.googleapis.com/css2?family=Playfair+Display:wght@700;900&family=Dancing+Script:wght@700&family=Cinzel:wght@400;700;900&display=swap">
<style>
  :root {
    --bg: #2c1210;
    --bg-leaf: #3d1916;
    --frame: #4a2622;
    --white: #ffffff;
    --orange: #f07f23;
    --maroon: #8b1a1a;
    --muted: #9c8b84;
    --ring: #f3c9a0;
    --leaf-red: #d63c24;
    --leaf-orange: #f0901e;
    --leaf-yellow: #f5cf18;
  }
  * { margin: 0; padding: 0; box-sizing: border-box; }
  html, body {
    width: 1200px;
    height: 2400px;
    overflow: hidden;
    background: var(--bg);
  }
  .label {
    position: relative;
    width: 1200px;
    height: 2400px;
    background: var(--bg);
    overflow: hidden;
  }
  .backdrop-leaf {
    position: absolute;
    left: 168px;
    width: 990px;
    height: 415px;
  }
  .backdrop-leaf--top { top: 0; }
  .backdrop-leaf--bottom { top: 1985px; }

  .brand {
    position: absolute;
    top: 490px;
    left: 0;
    width: 1200px;
    text-align: center;
  }
  .brand__first {
    display: block;
    font-family: "Playfair Display", Georgia, serif;
    font-weight: 900;
    font-size: 128px;
    line-height: 120px;
    color: var(--white);
  }
  .brand__rest {
    display: block;
    margin-top: -14px;
    font-family: "Dancing Script", cursive;
    font-weight: 700;
    font-size: 104px;
    line-height: 100px;
    color: var(--orange);
  }

  .frame {
    position: absolute;
    left: 0;
    top: 0;
    width: 1200px;
    height: 2400px;
  }
  .wreath {
    position: absolute;
    left: 79px;
    top: 755px;
    width: 1044px;
    height: 1048px;
  }
  .seal {
    position: absolute;
    left: 298px;
    top: 955px;
    width: 616px;
    height: 616px;
    border-radius: 50%;
    background: var(--white);
  }
  .seal::after {
    content: "";
    position: absolute;
    inset: 19px;
    border-radius: 50%;
    border: 1px solid var(--ring);
  }
  .seal__text {
    position: absolute;
    left: 0;
    width: 616px;
    text-align: center;
  }
  .seal__eyebrow {
    top: 100px;
    font-family: "Cinzel", Georgia, serif;
    font-weight: 400;
    font-size: 38px;
    letter-spacing: 4px;
    color: var(--muted);
  }
  .seal__title {
    top: 140px;
    font-family: "Dancing Script", cursive;
    font-weight: 700;
    font-size: 190px;
    line-height: 200px;
    color: var(--maroon);
  }
  .seal__subtitle {
    top: 325px;
    font-family: "Playfair Display", Georgia, serif;
    font-weight: 700;
    font-size: 118px;
    line-height: 120px;
    color: var(--maroon);
  }
  .seal__tagline {
    top: 488px;
    font-family: "Cinzel", Georgia, serif;
    font-weight: 400;
    font-size: 38px;
    letter-spacing: 4px;
    color: var(--muted);
  }
  .grade {
    position: absolute;
    top: 1845px;
    left: 0;
    width: 1200px;
    text-align: center;
    font-family: "Cinzel", Georgia, serif;
    font-weight: 900;
    font-size: 60px;
    line-height: 64px;
    color: var(--orange);
  }
</style>
</head>
<body>
<main class="label">
  <svg class="backdrop-leaf backdrop-leaf--top" role="img" aria-label="Faint large maple leaf silhouette" viewBox="0 0 990 415">
    <defs>
      <radialGradient id="faintTop" cx="50%" cy="30%" r="60%">
        <stop offset="0%" stop-color="#3d1916"/>
        <stop offset="100%" stop-color="#3d1916" stop-opacity="0"/>
      </radialGradient>
    </defs>
    <rect width="990" height="415" fill="url(#faintTop)"/>
  </svg>

  <h1 class="brand">
    <span class="brand__first">Quill</span>
    <span class="brand__rest">Hollow Maple</span>
  </h1>

  <svg class="frame" viewBox="0 0 1200 2400" aria-hidden="true">
    <path d="M284 1878 H137 V710 H1062 V1878 H918" fill="none" stroke="var(--frame)" stroke-width="1.5"/>
  </svg>

  <svg class="wreath" role="img" aria-label="Wreath of red, orange and yellow autumn maple leaves with outlined leaves behind" viewBox="0 0 1044 1048">
    <defs>
      <radialGradient id="wreathGlow" cx="50%" cy="50%" r="50%">
        <stop offset="45%" stop-color="var(--leaf-orange)"/>
        <stop offset="70%" stop-color="var(--leaf-red)" stop-opacity="0.9"/>
        <stop offset="85%" stop-color="var(--leaf-yellow)" stop-opacity="0.6"/>
        <stop offset="100%" stop-color="var(--leaf-yellow)" stop-opacity="0"/>
      </radialGradient>
    </defs>
    <ellipse cx="522" cy="500" rx="500" ry="500" fill="url(#wreathGlow)"/>
  </svg>

  <section class="seal">
    <p class="seal__text seal__eyebrow">100% PURE</p>
    <h2 class="seal__text seal__title">Maple</h2>
    <p class="seal__text seal__subtitle">Syrup</p>
    <p class="seal__text seal__tagline">RICH TASTE</p>
  </section>

  <p class="grade">GRADE A / AMBER</p>

  <svg class="backdrop-leaf backdrop-leaf--bottom" role="img" aria-label="Faint large maple leaf silhouette" viewBox="0 0 990 415">
    <defs>
      <radialGradient id="faintBottom" cx="50%" cy="70%" r="60%">
        <stop offset="0%" stop-color="#3d1916"/>
        <stop offset="100%" stop-color="#3d1916" stop-opacity="0"/>
      </radialGradient>
    </defs>
    <rect width="990" height="415" fill="url(#faintBottom)"/>
  </svg>
</main>
</body>
</html>
```